Broschüre für unsere Firma
Zielgruppe
Wäscherei Kranwitz / Textilservice
Geschäftskunden
Logos etc. In OneDrive/ Dropbox
https://dateiablage-nord.de/f/x7KpQm2Rv9TzLw4NcYh3
Wir wollen gerne eine 4 seitige Broschüre erstellen lassen, um unsere Firma vorzustellen.
Insbesondere der Service
Berufsbekleidung
Hygiene Gardienenwäsche Service
Hotelmietwäsche
Mitbewerb
http://www.wäscherei-gondelsack.de/index.php/ct-menu-item-17/ct-menu-item-25
http://www.waesche-tulpa.ch/download
Im Anhang finden Sie Bilder Logo und Flyers welche wir mal selbst gemacht haben!
Datein sind im OneDrive
Aufgabenstellung

```html
<!DOCTYPE html>
<html lang="de">
<head>
<meta charset="utf-8">
<title>Wäscherei Kranwitz – Broschüre</title>
<link rel="stylesheet" href="https://fonts.googleapis.com/css2?family=Cinzel:wght@400;600&family=Open+Sans:wght@400;600;700&display=swap">
<style>
  :root {
    --bg: #e6e7e9;
    --leaf: #d3e8a8;
    --leaf-light: #e4f1c6;
    --ink: #1b1b1b;
    --ink-soft: #333;
    --brand-blue: #1f3e8f;
    --badge-green: #2f8a3e;
    --white-veil: rgba(255,255,255,0.72);
  }
  * { box-sizing: border-box; margin: 0; padding: 0; }
  html, body { width: 1200px; height: 900px; overflow: hidden; }
  body {
    background: var(--bg);
    font-family: "Open Sans", Arial, sans-serif;
    color: var(--ink);
    position: relative;
  }

  /* ---------- Cover ---------- */
  .cover {
    position: absolute; left: 366px; top: 20px;
    width: 468px; height: 360px;
    box-shadow: 0 6px 18px rgba(0,0,0,.18);
    overflow: hidden;
  }
  .cover-photo {
    position: absolute; inset: 0;
    background: linear-gradient(100deg, #6f6f6f 0%, #bdbdbd 35%, #e2e2e2 50%, #9a9a9a 75%, #5a5a5a 100%);
  }
  .cover-band {
    position: absolute; left: 124px; top: 0; width: 220px; height: 100%;
    background: var(--white-veil);
    display: flex; flex-direction: column; align-items: center;
  }
  .brand {
    margin-top: 60px;
    display: flex; align-items: center; gap: 8px;
  }
  .brand-dot {
    width: 22px; height: 22px; border-radius: 50%;
    background: var(--brand-blue); flex: none;
  }
  .brand-name {
    font-weight: 700; font-size: 15px; color: var(--brand-blue);
    white-space: nowrap;
  }
  .cover-claim {
    margin-top: 80px; text-align: center;
    font-size: 16px; letter-spacing: 1.5px; line-height: 1.6;
    color: var(--ink);
  }
  .cover-claim strong { font-weight: 700; }

  /* ---------- Inner spread ---------- */
  .spread {
    position: absolute; left: 40px; top: 410px;
    width: 1120px; height: 460px;
    display: flex;
    box-shadow: 0 6px 18px rgba(0,0,0,.18);
  }
  .page { position: relative; width: 560px; height: 460px; }
  .page-left {
    background: linear-gradient(135deg, var(--leaf-light), var(--leaf));
    display: flex; gap: 30px; padding: 26px 30px 0 34px;
  }
  .page-right { display: flex; }
  .page-right .panel-text {
    width: 280px; background: var(--leaf);
    padding: 30px 22px 0;
  }
  .page-right .panel-photo { width: 280px; }

  .col-intro { width: 226px; display: flex; flex-direction: column; }
  .col-services { width: 240px; display: flex; flex-direction: column; padding-top: 4px; }

  .intro-title {
    font-family: "Cinzel", Georgia, serif;
    font-size: 30px; line-height: 1.05; letter-spacing: 3px;
  }
  .intro-lead {
    margin-top: 12px; width: 200px;
    font-weight: 700; font-size: 14px; line-height: 1.3;
  }
  .badges { margin-top: 16px; display: flex; gap: 10px; }
  .badge-square { width: 80px; height: 80px; background: var(--badge-green); }
  .badge-round { width: 60px; height: 60px; border-radius: 50%; background: var(--badge-green); margin-top: 30px; }

  .section-title { font-weight: 700; font-size: 12.5px; margin-bottom: 8px; line-height: 1.3; }
  .section-text { font-size: 10.5px; line-height: 1.45; color: var(--ink-soft); }
  .block-curtains { margin-top: 18px; padding-left: 30px; }

  .photo { display: block; }
  .photo-doctor {
    margin-top: 20px; width: 190px; height: 130px;
    background: linear-gradient(135deg, #c9d3d8, #f2f2f0 55%, #9fb3bd);
  }
  .photo-curtain {
    margin-top: 16px; width: 170px; height: 118px;
    background: linear-gradient(90deg, #7a6558, #d8cfc6 50%, #f4f2ee);
  }
  .photo-bed {
    margin-top: 24px; width: 236px; height: 120px;
    background: linear-gradient(135deg, #e9c6bd, #f7efe9 50%, #c9b9a8);
  }
  .photo-laundress {
    width: 100%; height: 100%;
    background: linear-gradient(160deg, #f3eee6, #ffffff 45%, #b7b4ae);
  }
</style>
</head>
<body>

  <section class="cover">
    <div class="cover-photo photo" role="img" aria-label="Schwarz-Weiß-Foto eines Waschsalons mit Reihen von Waschmaschinen"></div>
    <div class="cover-band">
      <div class="brand">
        <span class="brand-dot"></span>
        <span class="brand-name">Wäscherei Kranwitz</span>
      </div>
      <p class="cover-claim">WO <strong>QUALITÄT</strong><br>BESTIMMEND IST</p>
    </div>
  </section>

  <section class="spread">
    <div class="page page-left">
      <div class="col-intro">
        <h2 class="intro-title">LOREM<br>IPSUM</h2>
        <p class="intro-lead">Testen Sie uns und überzeugen Sie sich von unserer Qualität.</p>
        <div class="badges">
          <span class="badge-square" role="img" aria-label="Zertifikatssiegel"></span>
          <span class="badge-round" role="img" aria-label="Hygienesiegel"></span>
        </div>
        <div class="photo photo-doctor" role="img" aria-label="Foto eines Arztes im weißen Kittel in einer Praxis"></div>
      </div>

      <div class="col-services">
        <div class="block-workwear">
          <h3 class="section-title">Berufsbekleidung</h3>
          <p class="section-text">Wenn es um die Sicherheit Ihrer Mitarbeiter geht, überlassen Sie nichts dem Zufall. Wir arbeiten nach aktuellen RKI-Richtlinien. Geschulte und kompetente Mitarbeiter stehen Ihnen bei Beschaffung und professioneller Textilpflege zur Verfügung.</p>
        </div>
        <div class="block-curtains">
          <h3 class="section-title">Hygiene Gardienenwäsche Service</h3>
          <p class="section-text">Lorem ipsum dolor sit amet, consectetur adipiscing elit. Ut aliquam mi vitae velit posuere mollis. Aliquam non felis in augue pulvinar venenatis nec a tortor. Nulla facilisi.</p>
        </div>
        <div class="photo photo-curtain" role="img" aria-label="Foto eines Fensters mit hellen Gardinen"></div>
      </div>
    </div>

    <div class="page page-right">
      <div class="panel-text">
        <h3 class="section-title">Hotelmietwäsche</h3>
        <p class="section-text">In Ihrem Hotel erwartet Ihre Gäste exklusives Ambiente, eine gute Küche und eine herzliche Atmosphäre. Gerne unterstützen wir Sie hier mit unseren Dienstleistungen aus der hygienezertifizierten Wäscherei!</p>
        <div class="photo photo-bed" role="img" aria-label="Foto einer Hotelangestellten beim Bettenmachen"></div>
      </div>
      <div class="panel-photo">
        <div class="photo photo-laundress" role="img" aria-label="Foto einer Mitarbeiterin mit weißem Handtuch vor Waschmaschinen"></div>
      </div>
    </div>
  </section>

</body>
</html>
```